Cool modern, tech Business card design

Looking for a new business card design for our Managed IT Services company. We would like 2 sides, with the logo one one side horizontally and then the information on the back in either vertical or horizontal. We want our colors from the logo incorporated but also would like to see the color gray in there as well.

Target Market(s)

IT, Information Technology, Tech, Service

Industry/Entity Type

It Service

Contact Information for Business Card

Carl Penner
Managing Partner
(P)555-271-4830 ext xxx
(F)555-271-4831
www.brixtelcore.com

Font styles to use
Sans Serif

Colors
959595
000000
ec1f27

Requirements
Must have
• Logo on one side with some nice design or pattern
• Information on back in either vertical or horizontal format
Nice to have
• For it to look cool, tech, modern, stand out.

```html
<!DOCTYPE html>
<html lang="en">
<head>
<meta charset="utf-8">
<title>Brixtelcore Business Card</title>
<link rel="stylesheet" href="https://fonts.googleapis.com/css2?family=Ubuntu:wght@400;500;700&display=swap">
<style>
  :root {
    --brand-red: #ec1f27;
    --deep-red: #c8102e;
    --brand-gray: #959595;
    --pattern-gray: #b3b3b3;
    --ink: #231f20;
    --paper: #ffffff;
    --card-shadow: rgba(0, 0, 0, 0.32);
  }
  * { margin: 0; padding: 0; box-sizing: border-box; }
  html, body { width: 1200px; height: 1200px; overflow: hidden; background: var(--paper); }
  body { position: relative; font-family: "Ubuntu", sans-serif; color: var(--ink); }

  .card {
    position: absolute; left: 198px; width: 804px; height: 519px;
    background: var(--paper); overflow: hidden;
    box-shadow: 14px 14px 18px -4px var(--card-shadow);
  }
  .card--front { top: 34px; }
  .card--back { top: 613px; }

  .band { position: absolute; left: 0; width: 804px; display: block; }
  .band__base { fill: var(--brand-gray); }
  .band__texture { fill: var(--pattern-gray); }

  .front-top { top: 0; height: 97px; }
  .front-bottom { top: 364px; height: 155px; }
  .back-top { top: 0; height: 96px; }
  .back-bottom { top: 362px; height: 157px; }

  .wordmark { position: absolute; display: flex; align-items: center; white-space: nowrap; }
  .wordmark__square { background: var(--deep-red); }
  .wordmark__name { font-weight: 500; color: var(--ink); letter-spacing: -0.01em; }

  .wordmark--front { left: 0; width: 100%; top: 258px; justify-content: center; gap: 16px; }
  .wordmark--front .wordmark__square { width: 30px; height: 30px; }
  .wordmark--front .wordmark__name { font-size: 66px; line-height: 1; }

  .wordmark--back { left: 56px; width: 270px; top: 200px; justify-content: center; gap: 10px; }
  .wordmark--back .wordmark__square { width: 18px; height: 18px; }
  .wordmark--back .wordmark__name { font-size: 38px; line-height: 1; }

  .divider { position: absolute; left: 372px; top: 117px; width: 2px; height: 226px; background: var(--deep-red); }

  .contact { position: absolute; left: 480px; top: 120px; }
  .contact__name { font-size: 34px; font-weight: 500; color: var(--deep-red); line-height: 1.1; letter-spacing: -0.01em; }
  .contact__title { font-size: 22px; margin-top: 4px; line-height: 1.2; }
  .contact__row { position: absolute; left: 0; display: flex; align-items: center; }
  .contact__row--phone { top: 104px; }
  .contact__row--web { top: 190px; }
  .contact__icon { position: absolute; left: -62px; width: 32px; height: 32px; }
  .contact__lines { font-size: 21px; line-height: 28px; white-space: nowrap; }
</style>
</head>
<body>

<section class="card card--front" aria-label="Card front">
  <svg class="band front-top" viewBox="0 0 804 97" role="img" aria-label="Gray band with light rounded-square lattice pattern on the right">
    <rect class="band__base" width="804" height="97"/>
    <polygon class="band__texture" points="330,0 804,0 804,97 242,97"/>
  </svg>
  <div class="wordmark wordmark--front">
    <span class="wordmark__square"></span>
    <span class="wordmark__name">brixtelcore</span>
  </div>
  <svg class="band front-bottom" viewBox="0 0 804 155" role="img" aria-label="Gray band with light rounded-square lattice pattern on the left">
    <rect class="band__base" width="804" height="155"/>
    <polygon class="band__texture" points="0,0 682,0 514,155 0,155"/>
  </svg>
</section>

<section class="card card--back" aria-label="Card back">
  <svg class="band back-top" viewBox="0 0 804 96" role="img" aria-label="Gray band with light rounded-square lattice pattern on the left">
    <rect class="band__base" width="804" height="96"/>
    <polygon class="band__texture" points="0,0 474,0 562,96 0,96"/>
  </svg>

  <div class="wordmark wordmark--back">
    <span class="wordmark__square"></span>
    <span class="wordmark__name">brixtelcore</span>
  </div>

  <div class="divider"></div>

  <div class="contact">
    <div class="contact__name">Carl Penner</div>
    <div class="contact__title">Managing Partner</div>

    <div class="contact__row contact__row--phone">
      <svg class="contact__icon" viewBox="0 0 32 32" aria-hidden="true">
        <rect x="6" y="6" width="20" height="20" rx="5" transform="rotate(45 16 16)" fill="none" stroke="#c8102e" stroke-width="1.8"/>
        <path d="M12 11.5c.8-.8 1.6-.6 2 .1l1 1.7c.3.6.1 1.1-.4 1.5l-.6.5c.6 1.4 1.6 2.4 3 3l.5-.6c.4-.5.9-.7 1.5-.4l1.7 1c.7.4.9 1.2.1 2-1.3 1.3-3.5 1-6-1.5s-2.8-4.7-1.5-6z" fill="#c8102e"/>
      </svg>
      <div class="contact__lines">(P)555-271-4830 ext xxx<br>(F)555-271-4831</div>
    </div>

    <div class="contact__row contact__row--web">
      <svg class="contact__icon" viewBox="0 0 32 32" aria-hidden="true" style="top:-2px">
        <rect x="6" y="6" width="20" height="20" rx="5" transform="rotate(45 16 16)" fill="none" stroke="#c8102e" stroke-width="1.8"/>
        <g fill="none" stroke="#c8102e" stroke-width="1.1">
          <circle cx="16" cy="16" r="6"/>
          <ellipse cx="16" cy="16" rx="2.6" ry="6"/>
          <line x1="10" y1="16" x2="22" y2="16"/>
          <line x1="11" y1="13" x2="21" y2="13"/>
          <line x1="11" y1="19" x2="21" y2="19"/>
        </g>
      </svg>
      <div class="contact__lines">www.brixtelcore.com</div>
    </div>
  </div>

  <svg class="band back-bottom" viewBox="0 0 804 157" role="img" aria-label="Gray band with light rounded-square lattice pattern on the right">
    <rect class="band__base" width="804" height="157"/>
    <polygon class="band__texture" points="118,0 804,0 804,157 242,157"/>
  </svg>
</section>

</body>
</html>
```